Scrubbing Paper Towel Company needs Label Design

We need a product label that wraps around a roll of scrubbing paper towels as a sticker label of individually wrapped rolls. The sticker label has dimensions of 11.5" x 6" (width x height). The company logo with the brand feel and color theme is attached.

This is mainly used for dishwashing. A very large section of the label should show dishwashing and cleaning. Two very similar products can be found here :
---> https://www.shopvantrel.example/Non-Scratch-Disposable-Dish-Washing-Scrubbing-KT47R/dp/Q5203LMNVA/ref=sr_1_9?keywords=scouring+sheet&qid=4802719355&sr=8-9
--->https://www.shopvantrel.example/Pilu-Fendra-Disposable-Dish-washing-Scrubbing/dp/Q5864TXHWD/ref=sr_1_15?keywords=scouring+sheet&qid=4802719355&sr=8-15

To be included in the label:

Key points:
Did you know? Sponges are the perfect place for bacteria growth! We're talking hundreds of different species of bacteria growing in your dishwashing sponge - just as bad as the inside of your toilet. So why use a dirty sponge over and over again? Why does it smell so bad? Yes your toilet is gross, but why should the sponge go overlooked?

The Quirra Wipe is a sanitary solution to this problem. Use it once, wash and reuse up to three times before throwing each sheet away - that's enough for 180 washes per roll! But don't limit yourself to dishwashing. It's great for scrubbing surfaces with hardened debris or even dry residue left from old spills. So go ahead, take a stand against bacteria and wash away knowing your kitchen is finally clean. Now that's sanitary!

Multipurpose Use:
Dishwashing
**(with example image/graphic)**
Cleaning Toilets
Cleaning Grills
Wiping Down Stoves
Cleaning Sinks
Cleaning Pet Bowls

60 Sheets
7.9" X 8.7" per sheet

Features:
Perforated for Easy Tear
Reusable
Liquid Absorbent
Non-Flammable
Cadmium Free
Kitchen Safe

```html
<!DOCTYPE html>
<html lang="en">
<head>
<meta charset="utf-8">
<title>Quirra Wipe – Roll Label</title>
<link href="https://fonts.googleapis.com/css2?family=Roboto:wght@400;700&family=Roboto+Condensed:ital,wght@1,700&display=swap" rel="stylesheet">
<style>
  :root{
    --bg-light:#2f45a8;
    --bg-dark:#1c2683;
    --white:#ffffff;
    --sky:#4ba6dc;
    --sky-edge:#2a66c4;
  }
  html,body{margin:0;padding:0;overflow:hidden;}
  body{width:1200px;height:626px;}
  .label{
    position:relative;width:1200px;height:626px;overflow:hidden;
    background:radial-gradient(ellipse at 25% 30%,var(--bg-light) 0%,#2638a0 45%,var(--bg-dark) 100%);
    color:var(--white);
    font-family:"Roboto",Arial,sans-serif;
  }
  .brand{position:absolute;left:80px;top:150px;width:360px;text-align:center;}
  .brand-name{display:block;font-weight:700;font-size:58px;line-height:1;letter-spacing:-0.5px;}
  .brand-tagline{display:block;margin-top:14px;font-weight:700;font-size:20px;}
  .multipurpose{
    position:absolute;left:218px;top:360px;width:188px;height:44px;
    transform:rotate(-13deg);
  }
  .multipurpose svg{position:absolute;left:0;top:0;}
  .multipurpose span{
    position:absolute;left:0;top:0;width:188px;line-height:44px;text-align:center;
    font-weight:700;font-size:17px;letter-spacing:.3px;
  }
  .feature{position:absolute;font-weight:700;font-size:17px;white-space:nowrap;transform:translateY(-50%);}
  .feature-dot{position:absolute;width:16px;height:16px;border-radius:50%;background:var(--white);transform:translate(-50%,-50%);}
  .did-you-know{
    position:absolute;left:787px;top:80px;margin:0;
    font-family:"Roboto Condensed",Arial,sans-serif;font-style:italic;font-weight:700;font-size:23px;
  }
  .story-line{position:absolute;font-size:16.5px;white-space:nowrap;transform:translateY(-50%);}
  .uses{position:absolute;left:0;top:0;}
  .use{position:absolute;width:110px;text-align:center;font-size:12px;line-height:14px;transform:translateX(-50%);}
  .use svg{display:block;margin:0 auto 6px;}
  .count{position:absolute;left:922px;top:488px;width:80px;text-align:center;}
  .count-number{display:block;font-size:56px;line-height:1;font-weight:400;}
  .count-unit{display:block;font-size:17px;margin-top:2px;}
  .size{position:absolute;left:1007px;top:503px;width:120px;text-align:center;font-size:17px;line-height:21px;}
</style>
</head>
<body>
<div class="label">

  <div class="brand">
    <span class="brand-name">Quirra Wipe</span>
    <span class="brand-tagline">Clean Smarter, Not Harder</span>
  </div>

  <div class="multipurpose">
    <svg width="188" height="58" viewBox="0 0 188 58">
      <path d="M0 0H188V44H108L100 56L92 44H0Z" fill="var(--sky)" stroke="var(--sky-edge)" stroke-width="2"/>
    </svg>
    <span>Multipurpose Use</span>
  </div>

  <span class="feature" style="right:513px;top:117px;">Perforated for Easy Tear</span>
  <span class="feature-dot" style="left:718px;top:119px;"></span>
  <span class="feature" style="right:523px;top:170px;">Reusable</span>
  <span class="feature-dot" style="left:715px;top:171px;"></span>
  <span class="feature" style="right:528px;top:222px;">Liquid Absorbent</span>
  <span class="feature-dot" style="left:703px;top:223px;"></span>
  <span class="feature" style="right:538px;top:274px;">Non-Flammable</span>
  <span class="feature-dot" style="left:687px;top:275px;"></span>
  <span class="feature" style="right:562px;top:326px;">Cadmium Free</span>
  <span class="feature-dot" style="left:670px;top:328px;"></span>
  <span class="feature" style="right:596px;top:378px;">Kitchen Safe</span>
  <span class="feature-dot" style="left:646px;top:380px;"></span>

  <h2 class="did-you-know">Did you know?</h2>
  <div class="story">
    <span class="story-line" style="left:778px;top:130px;">Sponges are the perfect place for bacteria growth!</span>
    <span class="story-line" style="left:773px;top:154px;">We're talking hundreds of different species of</span>
    <span class="story-line" style="left:769px;top:177px;">bacteria growing in your dishwashing sponge - just</span>
    <span class="story-line" style="left:764px;top:200px;">as bad as the inside of your toilet. So why use a dirty</span>
    <span class="story-line" style="left:759px;top:223px;">sponge over and over again? Why does it smell so</span>
    <span class="story-line" style="left:754px;top:247px;word-spacing:8px;">bad? Yes your toilet is gross, but why should the</span>
    <span class="story-line" style="left:745px;top:270px;">sponge go overlooked?</span>

    <span class="story-line" style="left:739px;top:305px;">The Quirra Wipe is a sanitary solution to this problem.</span>
    <span class="story-line" style="left:734px;top:328px;">Use it once, wash and reuse up to three times before</span>
    <span class="story-line" style="left:724px;top:351px;">throwing each sheet away - that's enough for 180 washes</span>
    <span class="story-line" style="left:710px;top:374px;">per roll! But don't limit yourself to dishwashing. It's great for</span>
    <span class="story-line" style="left:700px;top:398px;">scrubbing surfaces with hardened debris or even dry residue</span>
    <span class="story-line" style="left:691px;top:421px;">left from old spills. So go ahead, take a stand against bacteria</span>
    <span class="story-line" style="left:681px;top:444px;">and wash away knowing your kitchen is finally clean. Now that's</span>
    <span class="story-line" style="left:681px;top:467px;">sanitary!</span>
  </div>

  <div class="uses">
    <div class="use" style="left:86px;top:492px;">
      <svg width="64" height="36" viewBox="0 0 64 36" fill="none" stroke="#fff" stroke-width="2.5">
        <ellipse cx="24" cy="24" rx="21" ry="10"/><ellipse cx="24" cy="24" rx="10" ry="4.5"/>
        <path d="M52 4l2 5 5 2-5 2-2 5-2-5-5-2 5-2z" stroke-width="1.8"/>
      </svg>Dishwashing
    </div>
    <div class="use" style="left:185px;top:476px;">
      <svg width="56" height="56" viewBox="0 0 56 56" fill="none" stroke="#fff" stroke-width="2.5">
        <rect x="10" y="3" width="18" height="20" rx="5"/><ellipse cx="19" cy="30" rx="14" ry="7"/>
        <path d="M7 32c2 10 6 14 12 14s10-4 12-14"/><path d="M13 46v7h12v-7"/>
        <path d="M44 10l2 5 5 2-5 2-2 5-2-5-5-2 5-2z" stroke-width="1.8"/>
      </svg>Cleaning<br>Toilets
    </div>
    <div class="use" style="left:276px;top:488px;">
      <svg width="60" height="44" viewBox="0 0 60 44" fill="none" stroke="#fff" stroke-width="2.5">
        <path d="M4 10h38M4 18h38M4 26h38M4 34h38M8 6v34M16 6v34M24 6v34M32 6v34M40 6v34"/>
        <path d="M50 4l2 5 5 2-5 2-2 5-2-5-5-2 5-2z" stroke-width="1.8"/>
      </svg>Cleaning<br>Grills
    </div>
    <div class="use" style="left:371px;top:488px;">
      <svg width="60" height="44" viewBox="0 0 60 44" fill="none" stroke="#fff" stroke-width="2.5">
        <rect x="4" y="16" width="38" height="24" rx="2"/><path d="M4 30h38"/>
        <ellipse cx="23" cy="22" rx="8" ry="3"/><circle cx="23" cy="35" r="2"/>
        <path d="M50 4l2 5 5 2-5 2-2 5-2-5-5-2 5-2z" stroke-width="1.8"/>
      </svg>Wiping<br>Down Stoves
    </div>
    <div class="use" style="left:466px;top:480px;">
      <svg width="56" height="52" viewBox="0 0 56 52" fill="none" stroke="#fff" stroke-width="2.5">
        <ellipse cx="20" cy="18" rx="16" ry="6"/><path d="M4 18c2 10 8 16 12 18v12h8V36c4-2 10-8 12-18"/>
        <path d="M44 4l2 5 5 2-5 2-2 5-2-5-5-2 5-2z" stroke-width="1.8"/>
      </svg>Cleaning<br>Sinks
    </div>
    <div class="use" style="left:553px;top:488px;">
      <svg width="56" height="44" viewBox="0 0 56 44" fill="none" stroke="#fff" stroke-width="2.5">
        <path d="M4 28c0 8 8 12 18 12s18-4 18-12z"/><path d="M8 28c2-6 6-9 14-9s12 3 14 9"/>
        <path d="M46 4l2 5 5 2-5 2-2 5-2-5-5-2 5-2z" stroke-width="1.8"/>
      </svg>Cleaning<br>Pet Bowls
    </div>
  </div>

  <div class="count">
    <span class="count-number">60</span>
    <span class="count-unit">Sheets</span>
  </div>
  <div class="size">7.9" X 8.7"<br>per sheet</div>

</div>
</body>
</html>
```